Stationary for Hair Cosmetic company

We mainly sell hair thickening products www.valmora-wohnstil.de/valmora-haar/ Hair thickening products are a smart and easy solution for thinning hair for both men and women. We sell very information oriented in an honest undramatic manner.

We would like to see a decent color and style that is suitable for men and women. It shall be rather modern with a vintage spin as our own product (Valmora Flask). Please use our logo (attatched).

Please bias your design to the bottle. To give you an idea: Chalk design like http://de.bildkorb-example.com/id/48213957 or one-color watercolor like http://de.bildkorb-example.com/id/63920581 is appreciated but not necessary.

Good but rejected designs will get compensation.

Target Market(s)

Wide range in demographics: age 20-55; 45% male, 55% women; issues with hair loss; self-conscious

Industry/Entity Type

Hair

Colors
3377b5
33a6d7
32b7a4
cbdf83
fbf289
fee18a
f9bb93
f05157

Requirements
Must have
• trustworthiness
Nice to have
• Chalk design like http://de.bildkorb-example.com/id/48213957 or one-color watercolor like http://de.bildkorb-example.com/id/63920581 is appreciated but not necessary

```html
<!DOCTYPE html>
<html lang="en">
<head>
<meta charset="utf-8">
<title>Valmora – Presentation Template</title>
<link href="https://fonts.googleapis.com/css2?family=Questrial&family=Lato:wght@400;700&family=Arimo:wght@400;700&display=swap" rel="stylesheet">
<style>
  :root {
    --backdrop-top: #c9c9c9;
    --backdrop-bottom: #a9a9a9;
    --paper: #f4f4f4;
    --paper-light: #fbfbfb;
    --ink-dark: #2f2d2e;
    --ink-band: #333132;
    --ink-text: #3a3a3a;
    --ink-body: #222222;
    --rule: #9a9a9a;
    --white: #ffffff;
    --ornament-tone: #3f3d3e;
    --badge-red: #d8262b;
    --badge-grey: #4a4a4a;
    --badge-yellow: #f2c11c;
    --badge-green: #6aa84f;
  }
  * { box-sizing: border-box; margin: 0; padding: 0; }
  html, body { width: 1200px; height: 1007px; overflow: hidden; }
  body {
    position: relative;
    background: radial-gradient(ellipse at 50% 35%, var(--backdrop-top), var(--backdrop-bottom));
    font-family: "Questrial", "Century Gothic", sans-serif;
  }
  .slide {
    position: absolute;
    width: 505px;
    height: 379px;
    background: linear-gradient(180deg, var(--paper-light), var(--paper));
    box-shadow: 4px 6px 10px rgba(0,0,0,.35);
    overflow: hidden;
  }
  .slide--title { left: 73px; top: 113px; }
  .slide--content-one { left: 613px; top: 113px; }
  .slide--closing { left: 73px; top: 525px; }
  .slide--content-two { left: 613px; top: 525px; }

  /* Brand mark */
  .brand { position: absolute; text-align: center; color: var(--ink-text); }
  .brand__circle {
    display: block; margin: 0 auto;
    border: 1.5px solid var(--ink-text); border-radius: 50%;
  }
  .brand__name {
    display: block; font-family: "Questrial", sans-serif;
    letter-spacing: 2px; color: var(--ink-text);
  }
  .brand--large { left: 0; right: 0; top: 24px; }
  .brand--large .brand__circle { width: 62px; height: 62px; }
  .brand--large .brand__name { font-size: 13px; margin-top: 34px; }
  .brand--small { right: 34px; top: 14px; width: 50px; }
  .brand--small .brand__circle { width: 34px; height: 34px; }
  .brand--small .brand__name { font-size: 7px; letter-spacing: 1px; margin-top: 24px; }

  /* Dark cover band */
  .cover-band { position: absolute; left: 0; right: 0; bottom: 0; top: 142px; }
  .cover-band__stripe { height: 10px; background: var(--ink-band); }
  .cover-band__gap { height: 4px; background: var(--white); }
  .cover-band__field {
    position: absolute; top: 14px; left: 0; right: 0; bottom: 0;
    background: var(--ink-dark);
  }
  .cover-band__ornament {
    position: absolute; right: 0; top: 8px; width: 110px; bottom: 0;
    background: linear-gradient(200deg, rgba(90,88,89,.0), rgba(90,88,89,.45) 55%, rgba(90,88,89,.1));
  }
  .slide--closing .cover-band { top: 143px; }
  .cover-band__title {
    position: absolute; left: 0; right: 0; text-align: center;
    color: var(--white); font-size: 26px; letter-spacing: .5px;
  }
  .cover-band__subtitle {
    position: absolute; left: 0; right: 0; text-align: center;
    color: var(--white); font-size: 14px;
  }
  .cover-band__url {
    position: absolute; left: 0; right: 0; bottom: 11px; text-align: center;
    color: var(--white); font-size: 12px;
  }

  /* Content slides */
  .section-tab { position: absolute; left: 0; top: 30px; }
  .section-tab__label {
    position: absolute; left: 38px; top: 3px;
    color: var(--white); font-size: 13px; font-family: "Questrial", sans-serif;
  }
  .footer-bar {
    position: absolute; left: 0; right: 0; bottom: 0; height: 11px;
    background: var(--ink-band);
  }
  .pie-chart { position: absolute; left: 40px; top: 120px; }
  .column-rule {
    position: absolute; left: 238px; top: 112px; width: 1px; height: 208px;
    background: var(--rule);
  }
  .body-copy {
    position: absolute; left: 257px; top: 107px; width: 240px;
    font-family: "Lato", sans-serif; font-size: 9.6px; line-height: 10.9px;
    color: var(--ink-body);
  }
  .label-copy {
    position: absolute; left: 87px; top: 78px; width: 310px;
    font-family: "Arimo", Arial, sans-serif; font-size: 8.3px; line-height: 9.6px;
    color: var(--ink-body);
  }
  .label-copy h3 { font-size: 8.6px; font-weight: 700; }
  .label-copy p { margin-bottom: 9px; }
  .label-copy .ingredients { font-size: 6.6px; line-height: 7.6px; }
  .batch {
    position: absolute; left: 89px; top: 303px;
    font-family: "Arimo", Arial, sans-serif; font-size: 8.5px; line-height: 10px;
    color: var(--ink-body);
  }
  .label-icons { position: absolute; left: 146px; top: 246px; }
</style>
</head>
<body>

  <!-- Title slide -->
  <section class="slide slide--title">
    <div class="brand brand--large">
      <span class="brand__circle"></span>
      <span class="brand__name">VALMORA</span>
    </div>
    <div class="cover-band">
      <div class="cover-band__stripe"></div>
      <div class="cover-band__gap"></div>
      <div class="cover-band__field">
        <div class="cover-band__ornament" role="img" aria-label="Faint feather ornament in dark grey"></div>
        <h1 class="cover-band__title" style="top:50px;">PRESENTATION TITLE</h1>
        <p class="cover-band__subtitle" style="top:84px;">PRESENTATION DATE</p>
        <p class="cover-band__url">www.valmora.com</p>
      </div>
    </div>
  </section>

  <!-- Content slide I -->
  <section class="slide slide--content-one">
    <svg class="section-tab" width="170" height="22" viewBox="0 0 170 22" aria-hidden="true">
      <polygon points="0,0 145,0 133,20 0,20" fill="var(--ink-band)"/>
      <polygon points="150,0 166,0 154,20 138,20" fill="var(--ink-band)"/>
    </svg>
    <span class="section-tab__label" style="top:33px;">content I</span>
    <div class="brand brand--small">
      <span class="brand__circle"></span>
      <span class="brand__name">VALMORA</span>
    </div>

    <svg class="pie-chart" width="180" height="180" viewBox="0 0 180 180" role="img" aria-label="Pie chart with eight segments">
      <g transform="translate(90,82) scale(1,0.88)">
        <g transform="translate(0,14)">
          <path d="M0 0 L13 -74 A75 75 0 0 1 70.5 -25.7 Z" fill="#7f9a1f" transform="translate(4,-16)"/>
          <path d="M0 0 L70.5 -25.7 A75 75 0 0 1 68 31.7 Z" fill="#1d5f99" transform="translate(4,0)"/>
          <path d="M0 0 L68 31.7 A75 75 0 0 1 25.7 70.5 Z" fill="#2c88ad" transform="translate(3,3)"/>
          <path d="M0 0 L25.7 70.5 A75 75 0 0 1 -31.7 68 Z" fill="#a81c1f" transform="translate(0,4)"/>
          <path d="M0 0 L-31.7 68 A75 75 0 0 1 -73.9 13 Z" fill="#b81d22" transform="translate(-3,3)"/>
          <path d="M0 0 L-73.9 13 A75 75 0 0 1 -68 -31.7 Z" fill="#c07a0d" transform="translate(-4,0)"/>
          <path d="M0 0 L-68 -31.7 A75 75 0 0 1 -43 -61.4 Z" fill="#c07a0d" transform="translate(-4,-2)"/>
          <path d="M0 0 L-43 -61.4 A75 75 0 0 1 13 -74 Z" fill="#b7b21a" transform="translate(-2,-4)"/>
        </g>
        <path d="M0 0 L13 -74 A75 75 0 0 1 70.5 -25.7 Z" fill="#9cc12e" transform="translate(4,-16)"/>
        <path d="M0 0 L70.5 -25.7 A75 75 0 0 1 68 31.7 Z" fill="#2a7ec0" transform="translate(4,0)"/>
        <path d="M0 0 L68 31.7 A75 75 0 0 1 25.7 70.5 Z" fill="#45b3de" transform="translate(3,3)"/>
        <path d="M0 0 L25.7 70.5 A75 75 0 0 1 -31.7 68 Z" fill="#dc2a2e" transform="translate(0,4)"/>
        <path d="M0 0 L-31.7 68 A75 75 0 0 1 -73.9 13 Z" fill="#e1262b" transform="translate(-3,3)"/>
        <path d="M0 0 L-73.9 13 A75 75 0 0 1 -68 -31.7 Z" fill="#ec9a1a" transform="translate(-4,0)"/>
        <path d="M0 0 L-68 -31.7 A75 75 0 0 1 -43 -61.4 Z" fill="#f0a21d" transform="translate(-4,-2)"/>
        <path d="M0 0 L-43 -61.4 A75 75 0 0 1 13 -74 Z" fill="#e6dd2c" transform="translate(-2,-4)"/>
      </g>
    </svg>

    <div class="column-rule"></div>
    <p class="body-copy">Lorem ipsum dolor sit amet, consectetur adipiscing elit. Duis sed aliquet neque. Fusce mollis placerat leo eu faucibus. Suspendisse suscipit egestas nunc, consequat euismod quam elementum venenatis. Nulla vitae nulla id mauris dictum imperdiet in vitae augue. Suspendisse fringilla bibendum ultrices. Sed rhoncus, nisi nec egestas tempus, orci velit ullamcorper dolor, malesuada molestie libero tellus in justo. Duis pharetra, turpis vel ultrices consequat, est ante laoreet nisi, et imperdiet ligula ipsum non quam. In tristique consequat diam, sed semper dolor aliquet et. Cum sociis natoque penatibus et magnis dis parturient montes, nascetur ridiculus mus. Duis sit amet ante mauris, a sodales tellus. Phasellus ante eros, lacinia at eleifend eu, laoreet sed nibh. Nulla rhoncus erat vitae dolor aliquam varius pretium lectus accumsan.</p>
    <div class="footer-bar"></div>
  </section>

  <!-- Closing slide -->
  <section class="slide slide--closing">
    <div class="brand brand--large">
      <span class="brand__circle"></span>
      <span class="brand__name">VALMORA</span>
    </div>
    <div class="cover-band">
      <div class="cover-band__stripe"></div>
      <div class="cover-band__gap"></div>
      <div class="cover-band__field">
        <div class="cover-band__ornament" role="img" aria-label="Faint feather ornament in dark grey"></div>
        <h1 class="cover-band__title" style="top:50px;font-size:24px;">THANK YOU</h1>
        <p class="cover-band__subtitle" style="top:84px;">...... For Your Times</p>
        <p class="cover-band__url">www.valmora.com</p>
      </div>
    </div>
  </section>

  <!-- Content slide II -->
  <section class="slide slide--content-two">
    <svg class="section-tab" width="170" height="22" viewBox="0 0 170 22" aria-hidden="true">
      <polygon points="0,0 145,0 133,20 0,20" fill="var(--ink-band)"/>
      <polygon points="150,0 166,0 154,20 138,20" fill="var(--ink-band)"/>
    </svg>
    <span class="section-tab__label" style="top:33px;">content II</span>
    <div class="brand brand--small">
      <span class="brand__circle"></span>
      <span class="brand__name">VALMORA</span>
    </div>

    <div class="label-copy">
      <h3>Anwendung / aplicacion / Application:</h3>
      <p>Fixierspray aus ca. 30 cm Abstand aufsprühen. Pumpe gelegentlich unter warmen Wasser reinigen.</p>
      <p>La fijación de la distanicia de pulverización de aproximadamente 30 cm. De vez encuando lipie la bomba con agua tibia.</p>
      <p>Apply the fixing spray from a 10 inches distance. Clean off nozzle from time to time.</p>
      <h3>Wichtig:</h3>
      <p>Nicht in die Augen und offene Flammen sprühen. Nur entleerte Flaschen in die Wertstoffsammlung geben. Entzündlich!</p>
      <h3>Ingredients:</h3>
      <p class="ingredients">Alcohol Denat., Acrylates/t-Butylacrylamide Copolymer, Panthenol, PEG-25 PABA, Aminomethylpropanol, Parfum, Hexylcinnamaldehyde, Benzyl Salicylate, Benzyl Benzoate, Dimethicone Copolyol.</p>
    </div>

    <p class="batch">Chargen-Nr.<br>361000914</p>

    <svg class="label-icons" width="240" height="100" viewBox="0 0 240 100" aria-label="Label symbols">
      <!-- period after opening -->
      <g transform="translate(0,54)">
        <path d="M2 6 L14 6 L14 16 L2 16 Z" fill="none" stroke="var(--badge-grey)" stroke-width="1.2"/>
        <path d="M4 6 L6 2 L10 2 L12 6" fill="none" stroke="var(--badge-grey)" stroke-width="1.2"/>
      </g>
      <!-- origin badge -->
      <path d="M30 52 Q60 36 88 44 L84 90 Q56 80 30 94 Z" fill="var(--badge-red)" opacity=".9" role="img" aria-label="Origin badge"/>
      <rect x="38" y="62" width="44" height="16" fill="var(--badge-grey)"/>
      <!-- ecology badge -->
      <circle cx="136" cy="71" r="24" fill="none" stroke="var(--badge-grey)" stroke-width="4" role="img" aria-label="Ecology badge"/>
      <circle cx="126" cy="92" r="5" fill="var(--badge-green)"/>
      <!-- animal testing badge -->
      <circle cx="189" cy="72" r="24" fill="var(--white)" stroke="var(--badge-red)" stroke-width="4" role="img" aria-label="Cruelty free badge"/>
      <line x1="172" y1="55" x2="206" y2="89" stroke="var(--badge-red)" stroke-width="4"/>
      <!-- flammable warning -->
      <g transform="translate(214,20)">
        <polygon points="0,-17 17,0 0,17 -17,0" fill="var(--white)" stroke="var(--badge-red)" stroke-width="2.5"/>
        <path d="M0 -8 C5 -3 6 2 4 6 L-4 6 C-6 2 -3 -2 0 -8 Z" fill="var(--ink-body)"/>
        <line x1="-6" y1="8" x2="6" y2="8" stroke="var(--ink-body)" stroke-width="1.5"/>
      </g>
    </svg>

    <div class="footer-bar"></div>
  </section>

</body>
</html>
```